Beautiful & Elegant Digital Brochure Needed For Luxury Real Estate Development

Hello,

Our company is seeking a beautiful design for our real estate development that is currently being launched.

About The Project:
Development Name - Harrow Mill Estate
Location - Charleston, S.C.
Low-Country Southern Style Architecture
Surfle "low-country" Charleston, SC to get an idea of the unique culture of the city
Surfle "copper birch tree" Charleston, SC to understand the branding

Other Digital Brochures that we love

http://www.vintrelodges.example/dunmerecove/wp-content/uploads/sites/6/2014/08/adventures-brochure.pdf

Why we like it... We love the classy feeling the brochure portrays by using unique fonts and backgrounds (burlap textures). We also love the images that represent a "low-country" vibe.

Requirements:
1. We will be providing all of the content (attached)

2. Please use plenty of southern low-country stock images from RapidLensPics (we have a subscription so just use the watermarked images unless you have full permissions)

3. Do not copy the Dunmere Cove brochure - create a unique vision that fits in to the low-country and southern vibe

4. Attached is our logos

The font we like to use is - Caslon Antique / italic
Thank you!

Target Market(s)

High net worth individuals - each homesite will be over 6 million dollars USD

Industry/Entity Type

Real Estate Development

Font styles to use
Script
Other font styles liked:
• Caslon Antique & Italic

Colors
abd036
00a990
acd036
9bcb3c
33b8a4
86cfc6
cfeae6

Requirements
Must have
• low country feeling
Nice to have
• burlap, wood backgrounds
Should not have
• Should NOT be corporate. This brochure is for multi-millionaire home buyers and investors. They are seeking simple, beautiful, quiet, serene, and southern lifestyles on the Intracoastal waterway on Wexley Cay, Charleston, South Carolina.

```html
<!DOCTYPE html>
<html lang="en">
<head>
<meta charset="utf-8">
<title>Harrow Mill Estate — Outdoor Living</title>
<link rel="stylesheet" href="https://fonts.googleapis.com/css2?family=Rye&family=Germania+One&family=Libre+Caslon+Text:ital,wght@0,400;0,700;1,400&family=IM+Fell+English+SC&display=swap">
<style>
  :root {
    --stage: #ffffff;
    --ink: #1a1712;
    --black: #050505;
    --gold: #c78a2a;
    --gold-light: #f3d57a;
    --gold-deep: #9c6416;
    --paper-top: #ffffff;
    --paper-mid: #ddd5c0;
    --paper-low: #b5a684;
    --grey-text: #9a9a9a;
  }
  * { box-sizing: border-box; margin: 0; padding: 0; }
  html, body { width: 1200px; height: 830px; overflow: hidden; background: var(--stage); }
  .spread { position: relative; width: 1200px; height: 830px; }
  .page {
    position: absolute; top: 24px; width: 552px; height: 782px;
    background: linear-gradient(180deg, var(--paper-top) 0%, var(--paper-top) 14%, var(--paper-mid) 55%, var(--paper-low) 100%);
    box-shadow: 0 1px 6px rgba(0,0,0,.35);
    overflow: hidden;
    font-family: "Libre Caslon Text", Georgia, serif;
    color: var(--ink);
  }
  .page-left { left: 38px; }
  .page-right { left: 619px; }
  .abs { position: absolute; }

  .gold-text {
    background: linear-gradient(180deg, var(--gold-light) 0%, var(--gold) 50%, var(--gold-deep) 100%);
    -webkit-background-clip: text; background-clip: text; color: transparent;
  }

  .title-band { left: 14px; top: 41px; width: 530px; height: 96px; background: var(--black);
    display: flex; align-items: center; justify-content: center; text-align: center; }
  .title-band h1 { font-family: "Rye", serif; font-weight: 400; font-size: 31px; line-height: 46px; letter-spacing: .5px; }

  .lead { left: 20px; top: 160px; width: 512px; text-align: center;
    font-family: "Germania One", serif; font-size: 20px; line-height: 25px; text-transform: uppercase; letter-spacing: .3px; }
  .intro-italic { left: 40px; top: 220px; width: 472px; text-align: center; font-style: italic; font-weight: 700; font-size: 12.3px; line-height: 17px; }
  .intro-body { left: 40px; top: 286px; width: 472px; text-align: center; font-size: 11.4px; line-height: 16px; }

  .photo { background: var(--ph); }
  .sunset-photo { left: 0; top: 340px; width: 552px; height: 124px;
    --ph: linear-gradient(180deg, rgba(255,255,255,0) 0%, #3b3a2a 18%, #0f120c 42%, #2a2a22 58%, #c9b07a 68%, #6d6650 82%, rgba(200,190,165,0) 100%); }

  .note-box { background: #fff; box-shadow: 0 0 4px rgba(0,0,0,.15); }
  .note-box::before, .note-box::after { content: ""; position: absolute; width: 10px; height: 10px;
    border: 2px solid #d8d2c4; }
  .note-box::before { left: -6px; top: -6px; }
  .note-box::after { right: -6px; bottom: -6px; }
  .docks { left: 50px; top: 468px; width: 468px; height: 154px; padding: 12px 10px 0; text-align: center; }
  .docks h2 { font-weight: 400; font-size: 19px; line-height: 24px; }
  .docks p { font-size: 11.4px; line-height: 16px; margin-top: 5px; }

  .plaque { left: 30px; top: 636px; width: 494px; height: 114px; }
  .plaque svg { position: absolute; inset: 0; }
  .plaque p { position: absolute; inset: 0; display: flex; align-items: center; justify-content: center; text-align: center;
    font-family: "Germania One", serif; font-size: 19px; line-height: 24px; text-transform: uppercase; color: var(--black); letter-spacing: .3px; }

  .garden-photo { left: 10px; top: 44px; width: 260px; height: 152px;
    --ph: radial-gradient(ellipse at 50% 60%, #6f9a86 0%, #3f6a2a 40%, #2f4d1e 70%, rgba(255,255,255,0) 100%); }
  .info-box { left: 287px; top: 46px; width: 242px; height: 148px; border: 1.5px solid var(--black); background: #fff;
    padding: 14px 6px 0; text-align: center; font-family: "IM Fell English SC", serif; font-size: 10.6px; line-height: 15.6px; letter-spacing: .4px; }
  .info-box .ib-head { font-family: "Germania One", serif; font-size: 13px; color: var(--ink); }
  .info-box .ib-grey { color: var(--grey-text); font-weight: 700; }
  .info-box .ib-gold { color: var(--gold); font-weight: 700; }

  .wildlife { left: 31px; top: 236px; width: 500px; font-weight: 700; font-size: 11.6px; line-height: 16px; }
  .birds { left: 31px; top: 314px; width: 230px; font-size: 11.4px; line-height: 15.8px; }
  .fawn-art { left: 300px; top: 292px; width: 220px; height: 150px;
    --ph: radial-gradient(ellipse at 55% 50%, #c98a45 0%, #b8925e 35%, rgba(170,160,130,.5) 60%, rgba(255,255,255,0) 75%); }

  .growth { left: 33px; top: 488px; width: 488px; height: 112px; display: flex; align-items: center; justify-content: center; text-align: center;
    font-family: "Germania One", serif; font-size: 14px; line-height: 19px; text-transform: uppercase; letter-spacing: .6px; padding: 0 10px; }

  .stewardship { left: 32px; top: 636px; width: 489px; height: 114px; background: var(--black);
    display: flex; align-items: center; justify-content: center; text-align: center; padding: 0 24px; }
  .stewardship p { font-size: 16.5px; line-height: 22px; }
</style>
</head>
<body>
<main class="spread">

  <section class="page page-left">
    <header class="abs title-band">
      <h1 class="gold-text">Embrace Outdoor Living<br>and Connect with Nature</h1>
    </header>

    <p class="abs lead">Life is better when lived outdoors and in<br>the Lowcountry, nature beckons.</p>

    <p class="abs intro-italic">Wake each morning to breathtaking sunrises and allow the warm, salt-kissed air to rejuvenate your soul.&nbsp; Spend your days enjoying one of the area’s exquisite beaches or visit some of Charleston’s inspiring heritage sites.</p>

    <p class="abs intro-body">During the early evenings, enjoy dinner alfresco before retiring on the veranda with family and friends.&nbsp; Gather around an outdoor fireplace to share the day’s memories and create even more under the stars.</p>

    <div class="abs photo sunset-photo" role="img" aria-label="Sunset over a tidal river with a dark treeline reflected in the water"></div>

    <article class="abs note-box docks">
      <h2 class="gold-text">Featuring both community and private docks,<br>Harrow Mill Estate is a maritime paradise.</h2>
      <p>Board your vessel to explore the tidal Stono River separating Wexley Cay from the mainland or follow the Intracoastal Waterway to the sea.&nbsp; For the adventurous, a kayak or canoe is an ideal means for exploring the intricacies of the island’s elaborate coastal marshes.&nbsp; Sport fishers will be pleased to find the channels teeming with flounder, cobia, mackerel, tarpon, white shrimp, and blue crabs.</p>
    </article>

    <div class="abs plaque">
      <svg viewBox="0 0 494 114" width="494" height="114" aria-hidden="true">
        <defs>
          <linearGradient id="plaqueGold" x1="0" y1="0" x2="1" y2="0">
            <stop offset="0" stop-color="#b8791c"/>
            <stop offset=".3" stop-color="#f6dc86"/>
            <stop offset=".6" stop-color="#d9a23e"/>
            <stop offset="1" stop-color="#a86a18"/>
          </linearGradient>
        </defs>
        <path d="M40 6 H454 Q460 20 476 22 Q476 40 490 57 Q476 74 476 92 Q460 94 454 108 H40 Q34 94 18 92 Q18 74 4 57 Q18 40 18 22 Q34 20 40 6 Z" fill="url(#plaqueGold)"/>
      </svg>
      <p>Non-anglers will also appreciate<br>the plentiful array of aquatic life and<br>availability of fresh daily seafood.</p>
    </div>
  </section>

  <section class="page page-right">
    <div class="abs photo garden-photo" role="img" aria-label="City garden with a tiered stone fountain among lush green trees"></div>

    <aside class="abs info-box">
      <div class="ib-head">Inland, Charleston County</div>
      <div class="ib-grey">is home to stunning city gardens, immaculate local parks, and quaint nature trails.</div>
      <div class="ib-gold">Terrestrial wildlife is plentiful on the island and even a short hike is likely to yield amazing photo opportunities.</div>
    </aside>

    <p class="abs wildlife">The island is heavily populated by South Carolina’s state animal, the white tailed deer, which can be seen bounding through the wooded terrain year-round. Wild turkeys, gray fox, flying squirrels, raccoon, bobcats, and<br>bear also call the island home.</p>

    <p class="abs birds">For bird watchers, a close eye on the skies will yield handsome rewards.&nbsp; Heron, osprey, bald eagles, red-tailed hawks egrets, and wood storks all call the island home. Dozens of migratory species provide increased variety to an already impressive host of island regulars and are always a welcome herald to the changing seasons.</p>

    <div class="abs photo fawn-art" role="img" aria-label="Spotted fawn running through grass"></div>

    <p class="abs note-box growth">Despite seeing an influx of visitors and new residents, a strong commitment to ecologically conscious growth promises that this natural wonderland will remain intact for generations to come.</p>

    <div class="abs stewardship">
      <p class="gold-text">Coastal management, wildlife conservation, and the protection of the area’s natural resources are paramount among the considerations and development is conducted responsibly and respectfully.</p>
    </div>
  </section>

</main>
</body>
</html>
```